Visitenkarten mit schwarzem Design gesucht
Zielgruppe
Zielgruppe sind Feinschmecker & Genießer.
Aufgabenstellung
Front schwarz mit unserem goldenen Logo. Rückseite auch in schwarz mit Firmenname, Adresse, Telefon, Email und Webadresse.
Es wäre klasse, wenn nach Beendigung des Projektes Datei für drei Ansprechpartner zur Verfügung gestellt werden. Das heißt, drei verschiedene Namen und Telefonnummern. Der Rest wäre dann gleichbleibend.
Bei der Gestaltung bitte bei der .eps Datei nur das Logo verwenden und nicht den Text!

```html
<!DOCTYPE html>
<html lang="de">
<head>
<meta charset="utf-8">
<title>Visitenkarten Quilvaro</title>
<link href="https://fonts.googleapis.com/css2?family=Open+Sans:wght@400;600;700&display=swap" rel="stylesheet">
<style>
  :root {
    --stage: #3a3a3a;
    --card: #141414;
    --edge: #e8ccaa;
    --gold: #d9b690;
    --gold-deep: #b88f65;
    --ghost: #2c2c2c;
  }
  * { margin: 0; padding: 0; box-sizing: border-box; }
  html, body { width: 1200px; height: 900px; overflow: hidden; }
  body {
    background: var(--stage);
    font-family: "Open Sans", sans-serif;
    position: relative;
  }
  .card {
    position: absolute;
    width: 640px;
    height: 372px;
    background: var(--card);
    border: 5px solid var(--edge);
    box-shadow: 0 10px 30px rgba(0,0,0,0.45);
  }
  .card-front { left: 90px; top: 50px; }
  .card-back { left: 470px; top: 478px; }

  .front-wordmark {
    position: absolute;
    left: 0; right: 0; top: 140px;
    text-align: center;
    color: var(--gold);
    font-weight: 700;
    font-size: 64px;
    letter-spacing: 1px;
  }
  .front-web {
    position: absolute;
    right: 40px; bottom: 26px;
    color: var(--gold);
    font-size: 15px;
    letter-spacing: 0.5px;
  }

  .back-wordmark {
    position: absolute;
    left: 30px; top: 148px;
    width: 270px;
    text-align: center;
    color: var(--ghost);
    font-weight: 700;
    font-size: 42px;
  }
  .back-divider {
    position: absolute;
    left: 312px; top: 60px;
    width: 3px; height: 250px;
    background: linear-gradient(to bottom, var(--gold) 0%, var(--gold-deep) 55%, rgba(184,143,101,0) 100%);
  }
  .contact {
    position: absolute;
    left: 352px; top: 58px;
    color: var(--gold);
  }
  .contact-name { font-weight: 700; font-size: 21px; letter-spacing: 0.3px; }
  .contact-role { font-size: 16px; margin-top: -2px; }
  .contact-address { margin-top: 52px; font-size: 17px; line-height: 25px; letter-spacing: 0.5px; }
  .contact-lines { margin-top: 26px; list-style: none; font-size: 17px; letter-spacing: 0.3px; }
  .contact-lines li { display: flex; align-items: center; height: 26px; white-space: nowrap; }
  .contact-lines svg { width: 16px; height: 16px; margin-right: 18px; flex: none; }
</style>
</head>
<body>
  <section class="card card-front">
    <div class="front-wordmark">Quilvaro</div>
    <div class="front-web">www.quilvaro-tisch.de</div>
  </section>

  <section class="card card-back">
    <div class="back-wordmark">Quilvaro</div>
    <div class="back-divider"></div>
    <div class="contact">
      <div class="contact-name">Vorname Name</div>
      <div class="contact-role">Position</div>
      <div class="contact-address">44715 Stadt<br>Stadtstraße 51</div>
      <ul class="contact-lines">
        <li>
          <svg viewBox="0 0 16 16" aria-hidden="true"><path d="M4 1.5 6 4.5 4.8 6.2c.8 1.8 2.2 3.2 4 4L10.5 9l3 2-1.2 2.6C7 13.3 2.7 9 2.4 3.7Z" fill="#d9b690"/></svg>
          +49 171-4826390
        </li>
        <li>
          <svg viewBox="0 0 16 16" aria-hidden="true"><rect x="1.5" y="3.5" width="13" height="9" fill="none" stroke="#d9b690" stroke-width="1.3"/><path d="M1.5 3.5 8 9l6.5-5.5" fill="none" stroke="#d9b690" stroke-width="1.3"/></svg>
          v.name@quilvaro-post.de
        </li>
        <li>
          <svg viewBox="0 0 16 16" aria-hidden="true"><g fill="none" stroke="#d9b690" stroke-width="1.2"><circle cx="8" cy="8" r="6.5"/><ellipse cx="8" cy="8" rx="3" ry="6.5"/><path d="M1.5 8h13M2.5 4.8h11M2.5 11.2h11"/></g></svg>
          www.quilvaro-tisch.de
        </li>
      </ul>
    </div>
  </section>
</body>
</html>
```